Bramwell Health Promotional flyer

Develop a professional flyer to be distributed to potential clients for consulting services.
Company name: Bramwell Health
see attachments for company logo and other bullet points . Bold items need to be on the flyer as written, other items can be tweaked/updated to sound more appealing.

```html
<!DOCTYPE html>
<html lang="en">
<head>
<meta charset="utf-8">
<title>Bramwell Health – Consulting Flyer</title>
<link href="https://fonts.googleapis.com/css2?family=Poppins:wght@400;600;700&family=Open+Sans:ital,wght@0,400;0,600;0,700;1,400&display=swap" rel="stylesheet">
<style>
:root{
  --backdrop:#2b323a;
  --paper:#ffffff;
  --blue:#0d5bbd;
  --blue-deep:#0a3f8c;
  --ink:#1d1d1f;
  --black:#000000;
  --muted:#5a6270;
  --photo-light:#eef4fa;
  --photo-mid:#b9cfe6;
}
*{margin:0;padding:0;box-sizing:border-box}
html,body{width:1200px;height:2736px;overflow:hidden;background:var(--backdrop)}
.flyer{
  position:absolute;left:100px;top:721px;width:856px;height:1108px;
  background:var(--paper);overflow:hidden;
  transform:scale(1.1682);transform-origin:top left;
  font-family:"Open Sans",Arial,sans-serif;color:var(--ink);
}
.abs{position:absolute}
.hero-photo{left:430px;top:0;width:426px;height:460px;
  background:radial-gradient(ellipse at 70% 40%,var(--photo-mid) 0%,#d6e4f2 45%,rgba(238,244,250,0) 80%);}
.cross-v{left:567px;top:0;width:60px;height:445px;background:var(--blue)}
.cross-h{left:445px;top:215px;width:411px;height:60px;background:var(--blue);
  clip-path:polygon(22px 0,100% 0,100% 100%,0 100%)}
.brand{left:83px;top:120px;display:flex;align-items:center;gap:14px}
.brand-mark{width:40px;height:40px;background:var(--blue)}
.brand-name{font-family:"Poppins",sans-serif;font-weight:700;font-size:40px;color:var(--blue);line-height:1}
.headline{left:83px;top:282px;font-family:"Poppins",sans-serif;line-height:1}
.headline .lead{font-size:47px;font-weight:400;color:var(--ink)}
.headline .strong{display:block;margin-top:6px;font-size:55px;font-weight:700;color:var(--blue)}
.band-services{left:0;top:422px;width:412px;height:38px;background:var(--blue);
  clip-path:polygon(0 0,100% 0,96% 100%,0 100%)}
.services-badge{left:76px;top:402px;width:82px;height:82px;border-radius:50%;background:var(--blue-deep);
  border:3px solid #fff;display:flex;align-items:center;justify-content:center}
.services-title{left:170px;top:424px;font-family:"Open Sans",sans-serif;font-weight:600;font-size:29px;color:#fff;line-height:34px}
.service-list{left:70px;top:497px;width:355px;list-style:none}
.service-list li{position:relative;padding-left:25px;font-size:13.6px;line-height:16px;margin-bottom:19px;text-align:justify}
.service-list li::before{content:"+";position:absolute;left:0;top:-6px;font-size:26px;font-weight:400;color:var(--blue)}
.service-list li.key{color:var(--blue);font-weight:600;letter-spacing:-.3px}
.band-why{left:0;top:756px;width:429px;height:40px;background:var(--black);
  clip-path:polygon(0 0,100% 0,95% 100%,0 100%)}
.why-title{left:80px;top:762px;font-weight:600;font-size:22px;color:#fff;line-height:28px}
.why-list{left:80px;top:808px;width:342px;list-style:none}
.why-list li{display:flex;align-items:center;gap:12px;padding:7px 0 9px;border-bottom:1.5px dashed #444;font-size:14px;line-height:16px}
.why-list li:last-child{border-bottom:none}
.why-list li.key{color:var(--blue);font-weight:600;letter-spacing:-.3px}
.why-list svg{flex:0 0 34px}
.portrait{left:463px;top:476px;width:126px;height:126px;border-radius:50%;
  background:radial-gradient(circle at 50% 40%,#e7d3c6 0%,#c9b3a6 35%,#4a5260 70%,#2f3540 100%);
  border:5px solid var(--blue)}
.bio-head{left:590px;top:528px;width:266px;height:38px;background:var(--blue);
  color:#fff;font-weight:600;font-size:21px;line-height:38px;padding-left:12px}
.bio-box{left:463px;top:572px;width:341px;height:396px;background:var(--blue);padding:20px 26px 0 22px}
.bio-list{list-style:none;color:#fff}
.bio-list li{position:relative;padding-left:16px;font-size:13.3px;line-height:15.5px;margin-bottom:16px;text-align:justify;font-weight:400}
.bio-list li::before{content:"";position:absolute;left:2px;top:3px;width:5px;height:9px;border:solid #fff;border-width:0 2px 2px 0;transform:rotate(45deg)}
.note{left:468px;top:978px;width:310px;font-style:italic;font-size:16px;line-height:16px;text-align:justify;display:flex;gap:8px}
.note svg{flex:0 0 22px}
.rule{left:0;top:1048px;width:500px;height:5px;background:var(--blue)}
.call-band{left:485px;top:1028px;width:371px;height:80px;background:var(--blue);
  clip-path:polygon(8px 0,100% 0,100% 100%,40px 100%,30px 50%)}
.call-icon{left:493px;top:1043px}
.call-text{left:536px;top:1040px;color:#fff;font-style:italic;line-height:1}
.call-text .label{font-size:16px;font-weight:400}
.call-text .number{display:block;margin-top:4px;font-size:30px;font-weight:700;letter-spacing:2px}
</style>
</head>
<body>
<main class="flyer">
  <div class="abs hero-photo" role="img" aria-label="Photo of a doctor holding a stethoscope with soft blue digital health icons"></div>
  <div class="abs cross-v"></div>
  <div class="abs cross-h"></div>

  <div class="abs brand">
    <span class="brand-mark"></span>
    <span class="brand-name">Bramwell Health</span>
  </div>

  <h1 class="abs headline"><span class="lead">Helping You Stay</span><span class="strong">HAPPY ONE</span></h1>

  <div class="abs band-services"></div>
  <div class="abs services-badge">
    <svg width="50" height="50" viewBox="0 0 50 50" fill="none" stroke="#fff" stroke-width="4" stroke-linecap="round">
      <path d="M12 6v14a11 11 0 0 0 22 0V6"/><path d="M23 31v4a8 8 0 0 0 16 0v-4"/><circle cx="39" cy="27" r="4"/>
    </svg>
  </div>
  <h2 class="abs services-title">SERVICES:</h2>

  <ul class="abs service-list">
    <li class="key">Retention of Emergency Medicine trained physician, Dr. Daniel K. Hollis MD for consultation on work-related injuries, illnesses or testing requirements.</li>
    <li class="key">Assist with occupational health risk management.</li>
    <li>Concierge level service and care at one of Dr. Hollis's 4 urgent care clinics when needed.</li>
    <li>Assistance setting up onsite clinics/ medics.</li>
    <li>Access to onsite services such as flu/covid vaccination clinics, onsite drug and alcohol testing, educational sessions, etc</li>
  </ul>

  <div class="abs band-why"></div>
  <h2 class="abs why-title">Why retain Bramwell Health</h2>
  <ul class="abs why-list">
    <li class="key">
      <svg width="34" height="34" viewBox="0 0 34 34" fill="none" stroke="#0d5bbd" stroke-width="2.5"><circle cx="17" cy="18" r="13"/><path d="M17 10v8l5 4" stroke-linecap="round"/><path d="M13 3h8"/></svg>
      24/7 access to a Medical Director</li>
    <li class="key">
      <svg width="34" height="34" viewBox="0 0 34 34"><path fill="#0d5bbd" d="M3 15h6v15H3zM11 15l6-10c2 0 3 1 3 3l-1 6h9c2 0 3 2 2 4l-3 9c-1 2-2 3-4 3H11z"/></svg>
      Reduction in recordable work-related injuries.</li>
    <li class="key">
      <svg width="34" height="34" viewBox="0 0 34 34" fill="none" stroke="#0d5bbd" stroke-width="2.5"><rect x="9" y="3" width="16" height="28" rx="3"/><path d="M14 15h6M17 12v6M14 27h6"/></svg>
      Concierge level service for your employees and managers</li>
    <li>
      <svg width="34" height="34" viewBox="0 0 34 34" fill="none" stroke="#0d5bbd" stroke-width="3" stroke-linecap="round"><path d="M6 4v9a8 8 0 0 0 16 0V4"/><path d="M14 21v3a6 6 0 0 0 12 0v-3"/><circle cx="26" cy="18" r="3"/></svg>
      Access to Bramwell Health's referral network of Imaging and Orthopedics and other providers</li>
  </ul>

  <div class="abs portrait" role="img" aria-label="Portrait photo of Dr. Hollis"></div>
  <h2 class="abs bio-head">DR.HOLLIS BIO</h2>
  <div class="abs bio-box">
    <ul class="bio-list">
      <li>Dr. Hollis grew up in Cedar Heights, Ohio and graduated from Westbrook Preparatory High School, Northfield State University and Lakeview Medical College.</li>
      <li>Dr. Hollis is Board Certified as a Diplomate of the National Board of Urgent Care Medicine and is a Fellow in the National Academy of Urgent Care Medicine.</li>
      <li>He practiced Emergency Medicine for 17 years at Maple Ridge Medical Center in Ashford Ohio.</li>
      <li>Dr. Hollis has practiced Urgent Care and Occupational Health Medicine for the last 29 years. He and his wife of 39 years have 3 children and live in Cedar Heights, Ohio.</li>
    </ul>
  </div>

  <p class="abs note">
    <svg width="22" height="22" viewBox="0 0 24 24"><path fill="#0d5bbd" d="M12 1l3.2 7 7.6.8-5.7 5.1 1.6 7.5L12 17.6 5.3 21.4l1.6-7.5L1.2 8.8 8.8 8z"/></svg>
    <span>Job sites do not need to be in Ohio for Dr. Hollis to provide consultative services.</span>
  </p>

  <div class="abs rule"></div>
  <div class="abs call-band"></div>
  <svg class="abs call-icon" width="40" height="40" viewBox="0 0 40 40" fill="none">
    <circle cx="20" cy="20" r="17" stroke="#fff" stroke-width="3" fill="#0d5bbd"/>
    <path fill="#fff" d="M13 11l4 0 2 5-2.5 2a12 12 0 0 0 5.5 5.5l2-2.5 5 2v4c-9 1-17-7-16-16z"/>
  </svg>
  <p class="abs call-text"><span class="label">CALL US NOW</span><span class="number">000 000 0000</span></p>
</main>
</body>
</html>
```